uLark

We need ideas for powerpoint template. Please submit several designs from simple/basic to elaborate/detailed using our company's logo. Please match designs with our logo color. We're very open to ideas. "Harbors Harmonized" can be removed

```html
<!DOCTYPE html>
<html lang="en">
<head>
<meta charset="utf-8">
<title>uLark – Slide Deck Template Overview</title>
<link href="https://fonts.googleapis.com/css2?family=Open+Sans:wght@400;600;700&family=Roboto:wght@400;500;700&display=swap" rel="stylesheet">
<style>
:root{
  --teal:#2f7f8e;
  --teal-dark:#1d5f6e;
  --teal-mid:#4a97a2;
  --teal-light:#5eb3ad;
  --mint:#7cc3bd;
  --ink:#222;
  --grey:#666;
  --line:#9fc7cf;
  --amber:#f5b400;
  --page:#e5e5e5;
  --white:#fff;
}
*{box-sizing:border-box;margin:0;padding:0}
html,body{width:1046px;height:1200px;overflow:hidden;background:var(--page)}
body{font-family:"Open Sans",Arial,sans-serif;color:var(--ink);position:relative}
.deck{position:absolute;left:12px;top:12px;display:grid;grid-template-columns:repeat(3,335px);grid-auto-rows:189px;gap:8px}
.slide{position:relative;background:var(--white);overflow:hidden}
.abs{position:absolute}
.title{position:absolute;left:0;right:0;text-align:center;color:var(--teal);font-family:Roboto,Arial,sans-serif;font-weight:500;font-size:13px}
.tx{font-size:3.6px;line-height:1.45;color:#333;text-align:justify}
.tx b{font-weight:700}
.brand{position:absolute;right:6px;top:5px;width:16px;text-align:center}
.brand i{display:block;width:12px;height:12px;margin:0 auto;border-radius:50%;background:var(--teal)}
.brand span{display:block;font-size:3px;color:var(--teal);font-weight:600;margin-top:1px}
.foot{position:absolute;left:3px;right:0;bottom:0;height:10px;border-top:1px solid var(--line);top:auto}
.foot .copy{position:absolute;left:2px;top:2px;font-size:2.4px;color:#777}
.foot .web{position:absolute;left:0;right:0;top:2px;text-align:center;font-size:2.4px;color:var(--teal)}
.foot .num{position:absolute;right:0;top:-6px;width:20px;height:9px;background:var(--teal);color:#fff;font-size:2.6px;text-align:center;line-height:9px}
.numlabel{position:absolute;font-family:Roboto,Arial,sans-serif;font-size:11px;color:#333}
.item{position:absolute;width:62px;border-left:1px solid #555;padding-left:4px}
.item h4{font-size:3.6px;font-weight:700;margin-bottom:1px}
.item p{font-size:3.2px;line-height:1.45;color:#666}
.sidebar{position:absolute;left:0;width:15px;background:var(--teal)}
.circle-num{position:absolute;width:14px;height:14px;border-radius:50%;border:1.5px solid var(--teal);font-size:4px;text-align:center;line-height:11px;color:var(--teal)}
table.fin{border-collapse:collapse;font-size:4px;font-family:Roboto,Arial,sans-serif}
table.fin td,table.fin th{height:8.7px;padding:0 2px;white-space:nowrap}
</style>
</head>
<body>
<div class="deck">

<!-- 1 cover with photo -->
<section class="slide">
  <div class="abs" style="left:0;right:0;top:30px;height:124px;background:linear-gradient(90deg,#2a7180,#4d939e)"></div>
  <div class="abs" role="img" aria-label="Photo of a green seedling growing from soil" style="left:26px;top:20px;width:114px;height:172px;border-radius:50% 45% 40% 55%/30% 40% 45% 45%;background:radial-gradient(circle at 45% 60%,#9a5a2c,#3a2a20 55%,#1d2220)"></div>
  <div class="abs" style="left:136px;top:90px;color:#fff;font-family:Roboto,Arial,sans-serif;font-weight:700;font-size:11px;letter-spacing:.2px">YOUR SLIDES DECK TITLE</div>
</section>

<!-- 2 cover network -->
<section class="slide">
  <div class="abs" role="img" aria-label="Dark teal network of connected dots" style="inset:0;clip-path:polygon(0 0,100% 0,100% 55%,0 82%);background:radial-gradient(circle at 70% 20%,#6fb6c9,#1f5e72 45%,#0e3748)"></div>
  <div class="abs" style="inset:0;clip-path:polygon(0 45%,100% 30%,100% 55%,0 82%);background:rgba(47,127,142,.75)"></div>
  <div class="abs" style="left:0;right:0;top:80px;text-align:center;color:#fff;font-family:Roboto,Arial,sans-serif;font-weight:700;font-size:16px">YOUR SLIDES DECK TITLE</div>
  <div class="abs" style="left:145px;top:118px;width:46px;height:46px;border-radius:50%;background:var(--teal);border:2px solid #fff"></div>
  <div class="abs" style="left:0;right:0;top:166px;text-align:center;color:var(--teal);font-size:10px;font-weight:600">uLark</div>
</section>

<!-- 3 cover name -->
<section class="slide">
  <div class="abs" role="img" aria-label="Teal background with faint network lines" style="left:0;right:0;top:8px;height:136px;background:radial-gradient(circle at 40% 40%,#4f97a8,#2a6f80 70%)"></div>
  <div class="abs" style="left:0;right:0;top:70px;text-align:center;color:#fff;font-family:Roboto,Arial,sans-serif;font-weight:700;font-size:14px">Your Slides Deck Name</div>
  <div class="abs" style="left:0;right:0;top:89px;text-align:center;color:#fff;font-size:6.5px">Your Slides Deck Name</div>
  <div class="abs" style="left:8px;top:150px;width:29px;height:29px;border-radius:50%;background:var(--teal);border:1.5px solid #fff;box-shadow:0 0 0 1px #cfe3e6"></div>
  <div class="abs" style="left:8px;top:179px;width:29px;text-align:center;font-size:5px;color:var(--teal);font-weight:600">uLark</div>
</section>

<!-- 4 about us -->
<section class="slide">
  <div class="brand"><i></i><span>uLark</span></div>
  <div class="title" style="top:16px">About Us</div>
  <div class="abs" style="left:130px;width:75px;top:35px;border-top:1px solid #888"></div>
  <div class="sidebar" style="top:57px;height:105px;width:16px"></div>
  <div class="abs tx" style="left:23px;top:58px;width:140px">Sed ut perspiciatis, unde omnis iste natus error sit voluptatem accusantium doloremque laudantium, totam rem aperiam eaque ipsa, quae ab illo inventore veritatis et quasi architecto beatae vitae dicta sunt, explicabo. <b>Nemo enim ipsam voluptatem,</b> quia voluptas sit, aspernatur aut odit aut fugit, sed quia consequuntur magni dolores eos, qui ratione <b>voluptatem sequi nesciunt,</b> neque porro quisquam est. Sed ut perspiciatis, unde omnis iste natus error sit voluptatem accusantium doloremque laudantium, totam rem aperiam eaque ipsa, quae ab illo inventore veritatis et quasi architecto beatae vitae dicta sunt, explicabo. <b>Nemo enim ipsam voluptatem,</b> quia voluptas sit, aspernatur aut odit aut fugit, sed quia consequuntur magni dolores eos, qui ratione <b>voluptatem sequi nesciunt,</b> neque porro quisquam est.</div>
  <div class="abs tx" style="left:173px;top:58px;width:150px">Sed ut perspiciatis, unde omnis iste natus error sit voluptatem accusantium doloremque laudantium, totam rem aperiam eaque ipsa, quae ab illo inventore veritatis et quasi architecto beatae vitae dicta sunt, explicabo. <b>Nemo enim ipsam voluptatem,</b> quia voluptas sit, aspernatur aut odit aut fugit, sed quia consequuntur magni dolores eos, qui ratione <b>voluptatem sequi nesciunt,</b> neque porro quisquam est. Sed ut perspiciatis, unde omnis iste natus error sit voluptatem accusantium doloremque laudantium, totam rem aperiam eaque ipsa, quae ab illo inventore veritatis et quasi architecto beatae vitae dicta sunt, explicabo. <b>Nemo enim ipsam voluptatem,</b> quia voluptas sit, aspernatur aut odit aut fugit, sed quia consequuntur magni dolores eos, qui ratione <b>voluptatem sequi nesciunt,</b> neque porro quisquam est.</div>
  <div class="foot"><span class="copy">Copyrighted content</span><span class="web">www.uLarkSlides.com</span><span class="num">5</span></div>
</section>

<!-- 5 two column text -->
<section class="slide">
  <div class="brand"><i></i><span>uLark</span></div>
  <div class="abs" style="left:19px;top:80px;color:var(--teal);font-family:Roboto,Arial,sans-serif;font-weight:500;font-size:12px">Lorem ipsum dolor</div>
  <div class="abs" style="left:68px;width:30px;top:98px;border-top:1px solid #888"></div>
  <div class="abs tx" style="left:140px;top:30px;width:86px">Lorem ipsum dolor sit amet, consectetur adipiscing elit, sed do eiusmod tempor incididunt ut labore et dolore magna aliqua. Ut enim ad minim veniam, quis nostrud exercitation ullamco laboris nisi ut aliquip ex ea commodo consequat. Lorem ipsum dolor sit amet, consectetur adipiscing elit, sed do eiusmod tempor incididunt ut labore et dolore magna aliqua. Lorem ipsum dolor sit amet, consectetur adipiscing elit, sed do eiusmod tempor incididunt ut labore et dolore magna aliqua. Ut enim ad minim veniam, quis nostrud exercitation ullamco laboris nisi ut aliquip ex ea commodo consequat. Lorem ipsum dolor sit amet, consectetur adipiscing elit, sed do eiusmod tempor incididunt ut labore et dolore magna aliqua.</div>
  <div class="abs tx" style="left:236px;top:30px;width:86px">Lorem ipsum dolor sit amet, consectetur adipiscing elit, sed do eiusmod tempor incididunt ut labore et dolore magna aliqua. Ut enim ad minim veniam, quis nostrud exercitation ullamco laboris nisi ut aliquip ex ea commodo consequat. Lorem ipsum dolor sit amet, consectetur adipiscing elit, sed do eiusmod tempor incididunt ut labore et dolore magna aliqua. Lorem ipsum dolor sit amet, consectetur adipiscing elit, sed do eiusmod tempor incididunt ut labore et dolore magna aliqua. Ut enim ad minim veniam, quis nostrud exercitation ullamco laboris nisi ut aliquip ex ea commodo consequat. Lorem ipsum dolor sit amet, consectetur adipiscing elit, sed do eiusmod tempor incididunt.</div>
  <div class="foot"><span class="copy">Copyrighted content</span><span class="web">www.uLarkSlides.com</span><span class="num">6</span></div>
</section>

<!-- 6 six items -->
<section class="slide">
  <div class="brand"><i></i><span>uLark</span></div>
  <div class="title" style="top:24px">Lorem ipsum dolor</div>
  <div class="abs" style="left:150px;width:60px;top:43px;border-top:1px solid #888"></div>
  <div class="sidebar" style="top:58px;height:105px"></div>
  <span class="numlabel" style="left:49px;top:68px">01</span><div class="item" style="left:67px;top:68px"><h4>Lorem ipsum dolor</h4><p>Lorem ipsum dolor sit amet, consectetur adipiscing elit, sed do eiusmod tempor</p></div>
  <span class="numlabel" style="left:131px;top:68px">02</span><div class="item" style="left:149px;top:68px"><h4>Lorem ipsum dolor</h4><p>Lorem ipsum dolor sit amet, consectetur adipiscing elit, sed do eiusmod tempor</p></div>
  <span class="numlabel" style="left:212px;top:68px">03</span><div class="item" style="left:230px;top:68px"><h4>Lorem ipsum dolor</h4><p>Lorem ipsum dolor sit amet, consectetur adipiscing elit, sed do eiusmod tempor</p></div>
  <span class="numlabel" style="left:49px;top:116px">04</span><div class="item" style="left:67px;top:116px"><h4>Lorem ipsum dolor</h4><p>Lorem ipsum dolor sit amet, consectetur adipiscing elit, sed do eiusmod tempor</p></div>
  <span class="numlabel" style="left:131px;top:116px">05</span><div class="item" style="left:149px;top:116px"><h4>Lorem ipsum dolor</h4><p>Lorem ipsum dolor sit amet, consectetur adipiscing elit, sed do eiusmod tempor</p></div>
  <span class="numlabel" style="left:212px;top:116px">06</span><div class="item" style="left:230px;top:116px"><h4>Lorem ipsum dolor</h4><p>Lorem ipsum dolor sit amet, consectetur adipiscing elit, sed do eiusmod tempor</p></div>
  <div class="foot"><span class="copy">Copyrighted content</span><span class="web">www.uLarkSlides.com</span><span class="num">7</span></div>
</section>

<!-- 7 eight items with band -->
<section class="slide">
  <div class="brand"><i></i><span>uLark</span></div>
  <div class="title" style="top:14px">Lorem ipsum dolor</div>
  <div class="abs" style="left:150px;width:60px;top:33px;border-top:1px solid #888"></div>
  <span class="numlabel" style="left:7px;top:48px">01</span><div class="item" style="left:25px;top:48px;width:55px"><h4>Lorem ipsum dolor</h4><p>Lorem ipsum dolor sit amet, consectetur adipiscing elit, sed do eiusmod tempor</p></div>
  <span class="numlabel" style="left:88px;top:48px">02</span><div class="item" style="left:106px;top:48px;width:55px"><h4>Lorem ipsum dolor</h4><p>Lorem ipsum dolor sit amet, consectetur adipiscing elit, sed do eiusmod tempor</p></div>
  <span class="numlabel" style="left:171px;top:48px">03</span><div class="item" style="left:189px;top:48px;width:55px"><h4>Lorem ipsum dolor</h4><p>Lorem ipsum dolor sit amet, consectetur adipiscing elit, sed do eiusmod tempor</p></div>
  <span class="numlabel" style="left:253px;top:48px">04</span><div class="item" style="left:271px;top:48px;width:55px"><h4>Lorem ipsum dolor</h4><p>Lorem ipsum dolor sit amet, consectetur adipiscing elit, sed do eiusmod tempor</p></div>
  <span class="numlabel" style="left:7px;top:92px">05</span><div class="item" style="left:25px;top:92px;width:55px"><h4>Lorem ipsum dolor</h4><p>Lorem ipsum dolor sit amet, consectetur adipiscing elit, sed do eiusmod tempor</p></div>
  <span class="numlabel" style="left:88px;top:92px">06</span><div class="item" style="left:106px;top:92px;width:55px"><h4>Lorem ipsum dolor</h4><p>Lorem ipsum dolor sit amet, consectetur adipiscing elit, sed do eiusmod tempor</p></div>
  <span class="numlabel" style="left:171px;top:92px">07</span><div class="item" style="left:189px;top:92px;width:55px"><h4>Lorem ipsum dolor</h4><p>Lorem ipsum dolor sit amet, consectetur adipiscing elit, sed do eiusmod tempor</p></div>
  <span class="numlabel" style="left:253px;top:92px">08</span><div class="item" style="left:271px;top:92px;width:55px"><h4>Lorem ipsum dolor</h4><p>Lorem ipsum dolor sit amet, consectetur adipiscing elit, sed do eiusmod tempor</p></div>
  <div class="abs" style="left:0;right:0;top:146px;height:43px;background:var(--teal-light);color:#fff;text-align:center;font-size:7px;font-weight:600;padding-top:11px;line-height:1.5">Lorem ipsum dolor sit amet, consectetur adipiscing elit,<br>sed do eiusmod tempor</div>
</section>

<!-- 8 agenda -->
<section class="slide">
  <div class="brand"><i></i><span>uLark</span></div>
  <div class="abs" style="left:43px;top:80px;color:var(--teal);font-family:Roboto,Arial,sans-serif;font-weight:500;font-size:17px">Agenda</div>
  <div class="abs" style="left:78px;width:26px;top:104px;border-top:1px solid #888"></div>
  <div class="abs" style="left:182px;top:37px">
    <div style="display:flex;align-items:center;height:20px"><span style="width:14px;height:14px;border-radius:50%;background:var(--teal-light);color:#fff;font-size:4px;text-align:center;line-height:14px;box-shadow:0 0 0 2px #cbe6e3">01</span><span style="font-size:4.6px;margin-left:10px">Lorem ipsum dolor sit amet</span></div>
    <div style="display:flex;align-items:center;height:20px"><span style="width:14px;height:14px;border-radius:50%;background:var(--teal-light);color:#fff;font-size:4px;text-align:center;line-height:14px;box-shadow:0 0 0 2px #cbe6e3">02</span><span style="font-size:4.6px;margin-left:10px">Lorem ipsum dolor sit amet</span></div>
    <div style="display:flex;align-items:center;height:20px"><span style="width:14px;height:14px;border-radius:50%;background:var(--teal-light);color:#fff;font-size:4px;text-align:center;line-height:14px;box-shadow:0 0 0 2px #cbe6e3">03</span><span style="font-size:4.6px;margin-left:10px">Lorem ipsum dolor sit amet</span></div>
    <div style="display:flex;align-items:center;height:20px"><span style="width:14px;height:14px;border-radius:50%;background:var(--teal-light);color:#fff;font-size:4px;text-align:center;line-height:14px;box-shadow:0 0 0 2px #cbe6e3">04</span><span style="font-size:4.6px;margin-left:10px">Lorem ipsum dolor sit amet</span></div>
    <div style="display:flex;align-items:center;height:20px"><span style="width:14px;height:14px;border-radius:50%;background:var(--teal-light);color:#fff;font-size:4px;text-align:center;line-height:14px;box-shadow:0 0 0 2px #cbe6e3">05</span><span style="font-size:4.6px;margin-left:10px">Lorem ipsum dolor sit amet</span></div>
    <div style="display:flex;align-items:center;height:20px"><span style="width:14px;height:14px;border-radius:50%;background:var(--teal-light);color:#fff;font-size:4px;text-align:center;line-height:14px;box-shadow:0 0 0 2px #cbe6e3">06</span><span style="font-size:4.6px;margin-left:10px">Lorem ipsum dolor sit amet</span></div>
  </div>
  <div class="foot"><span class="copy">Copyrighted content</span><span class="web">www.uLarkSlides.com</span><span class="num">9</span></div>
</section>

<!-- 9 case studies -->
<section class="slide">
  <div class="brand"><i></i><span>uLark</span></div>
  <div class="title" style="top:14px">Case Studies</div>
  <div class="abs" style="left:150px;width:60px;top:33px;border-top:1px solid #888"></div>
  <div class="abs tx" style="left:18px;top:48px;width:142px;text-align:left">Lorem ipsum dolor sit amet, consectetur adipiscing elit, sed do eiusmod tempor incididunt ut labore et dolore magna aliqua. Ut enim ad minim veniam, quis nostrud exercitation ullamco laboris nisi ut aliquip ex</div>
  <div class="abs tx" style="left:18px;top:79px;width:124px;height:56px;background:linear-gradient(90deg,#3b8897,#5ea7ae);color:#fff;padding:10px 5px;text-align:left">Lorem ipsum dolor sit amet, consectetur adipiscing elit, sed do eiusmod tempor incididunt ut labore et dolore magna aliqua. Ut enim ad minim veniam, quis nostrud exercitation ullamco laboris nisi ut aliquip ex</div>
  <div class="abs tx" style="left:18px;top:142px;width:142px;text-align:left">Lorem ipsum dolor sit amet, consectetur adipiscing elit, sed do eiusmod tempor incididunt ut labore et dolore magna aliqua. Ut enim ad minim veniam, quis nostrud exercitation ullamco laboris nisi ut aliquip ex</div>
  <div class="circle-num" style="left:190px;top:47px;width:17px;height:17px;line-height:14px">01</div>
  <div class="circle-num" style="left:190px;top:76px;width:17px;height:17px;line-height:14px">02</div>
  <div class="circle-num" style="left:190px;top:106px;width:17px;height:17px;line-height:14px">03</div>
  <div class="circle-num" style="left:190px;top:135px;width:17px;height:17px;line-height:14px">04</div>
  <div class="abs" style="left:213px;top:45px;width:110px;font-size:3.3px;line-height:1.4"><b style="color:var(--teal)">Your Text Here</b><br>Lorem ipsum dolor sit amet, consectetur adipiscing elit, sed do eiusmod tempor incididunt ut labore et dolore magna aliqua.</div>
  <div class="abs" style="left:213px;top:74px;width:110px;font-size:3.3px;line-height:1.4"><b style="color:var(--teal)">Your Text Here</b><br>Lorem ipsum dolor sit amet, consectetur adipiscing elit, sed do eiusmod tempor incididunt ut labore et dolore magna aliqua.</div>
  <div class="abs" style="left:213px;top:104px;width:110px;font-size:3.3px;line-height:1.4"><b style="color:var(--teal)">Your Text Here</b><br>Lorem ipsum dolor sit amet, consectetur adipiscing elit, sed do eiusmod tempor incididunt ut labore et dolore magna aliqua.</div>
  <div class="abs" style="left:213px;top:133px;width:110px;font-size:3.3px;line-height:1.4"><b style="color:var(--teal)">Your Text Here</b><br>Lorem ipsum dolor sit amet, consectetur adipiscing elit, sed do eiusmod tempor incididunt ut labore et dolore magna aliqua.</div>
  <div class="foot"><span class="copy">Copyrighted content</span><span class="web">www.uLarkSlides.com</span><span class="num">10</span></div>
</section>

<!-- 10 process chevrons -->
<section class="slide">
  <div class="brand"><i></i><span>uLark</span></div>
  <div class="title" style="top:24px">Title Goes Here</div>
  <div class="abs" style="left:150px;width:60px;top:43px;border-top:1px solid #888"></div>
  <svg class="abs" style="left:0;top:55px" width="335" height="100" viewBox="0 0 335 100">
    <g fill="none" stroke="#222" stroke-width="2">
      <circle cx="60" cy="20" r="6"/><circle cx="60" cy="20" r="2"/>
      <ellipse cx="132" cy="20" rx="9" ry="3.5"/><ellipse cx="132" cy="20" rx="9" ry="3.5" transform="rotate(60 132 20)"/><ellipse cx="132" cy="20" rx="9" ry="3.5" transform="rotate(-60 132 20)"/>
    </g>
    <path d="M209 11h6M210 11v7l-6 10h16l-6-10v-7" fill="var(--teal-light)" stroke="#222" stroke-width="1.5"/>
    <path d="M275 12l11 10-4 4-10-11z" fill="#222"/><path d="M272 24l-4 4M276 27l-3 4" stroke="#222" stroke-width="1.5"/>
    <g font-family="Roboto,Arial,sans-serif" font-size="4.6" font-weight="700" text-anchor="middle">
      <polygon points="38,41 108,41 116,49 108,57 38,57 44,49" fill="#fff" stroke="#888" stroke-width=".6"/><text x="77" y="51" fill="#333">Contents Title</text>
      <polygon points="109,41 179,41 187,49 179,57 109,57 115,49" fill="#fff" stroke="#888" stroke-width=".6"/><text x="148" y="51" fill="#333">Contents Title</text>
      <polygon points="180,41 250,41 258,49 250,57 180,57 186,49" fill="var(--teal)"/><text x="219" y="51" fill="#fff">Contents Title</text>
      <polygon points="251,41 321,41 329,49 321,57 251,57 257,49" fill="#fff" stroke="#888" stroke-width=".6"/><text x="290" y="51" fill="#333">Contents Title</text>
    </g>
  </svg>
  <div class="abs" style="left:38px;top:123px;width:290px;display:flex;justify-content:space-between;text-align:center;font-size:3.5px;line-height:1.45;color:#444">
    <p style="width:62px">Lorem ipsum dolor sit amet, consectetur adipiscing elit, sed do eiusmod tempor incididunt ut labore et dolore magna aliqua.</p>
    <p style="width:62px">Lorem ipsum dolor sit amet, consectetur adipiscing elit, sed do eiusmod tempor incididunt ut labore et dolore magna aliqua.</p>
    <p style="width:62px">Lorem ipsum dolor sit amet, consectetur adipiscing elit, sed do eiusmod tempor incididunt ut labore et dolore magna aliqua.</p>
    <p style="width:62px">Lorem ipsum dolor sit amet, consectetur adipiscing elit, sed do eiusmod tempor incididunt ut labore et dolore magna aliqua.</p>
  </div>
  <div class="foot"><span class="copy">Copyrighted content</span><span class="web">www.uLarkSlides.com</span><span class="num">11</span></div>
</section>

<!-- 11 three columns with feature box -->
<section class="slide">
  <div class="brand"><i></i><span>uLark</span></div>
  <div class="title" style="top:12px">Title Goes Here</div>
  <div class="abs" style="left:150px;width:60px;top:31px;border-top:1px solid #888"></div>
  <div class="abs tx" style="left:23px;top:39px;width:88px;text-align:left">Lorem ipsum dolor sit amet, consectetur adipiscing elit, sed do eiusmod tempor incididunt ut labore et dolore magna aliqua. Ut enim ad minim veniam, quis nostrud exercitation ullamco laboris nisi ut aliquip ex.<br><br>ea commodo consequat. Lorem ipsum dolor sit amet, consectetur adipiscing elit, sed do eiusmod tempor incididunt ut labore et dolore magna aliqua.<br><br>Lorem ipsum dolor sit amet, consectetur adipiscing elit, sed do eiusmod tempor incididunt ut labore et dolore magna aliqua. Ut enim ad minim veniam.</div>
  <div class="abs tx" style="left:125px;top:39px;width:88px;text-align:left">Lorem ipsum dolor sit amet, consectetur adipiscing elit, sed do eiusmod tempor incididunt ut labore et dolore magna aliqua. Ut enim ad minim veniam, quis nostrud exercitation ullamco.</div>
  <div class="abs" style="left:125px;top:88px;width:88px;height:101px;background:var(--teal-light);color:#fff;padding:8px 5px">
    <svg width="88" height="18" viewBox="0 0 78 18" style="display:block"><rect x="33" y="1" width="11" height="16" rx="2" fill="none" stroke="#fff" stroke-width="1.4"/></svg>
    <div style="text-align:center;font-size:4.4px;font-weight:700;margin:3px 0">Lorem ipsum dolor</div>
    <div class="tx" style="color:#fff">Lorem ipsum dolor sit amet, consectetur adipiscing elit, sed do eiusmod tempor incididunt ut labore et dolore magna aliqua. Ut enim ad minim veniam, quis nostrud exercitation ullamco laboris nisi ut aliquip ex ea commodo consequat.</div>
  </div>
  <div class="abs tx" style="left:233px;top:39px;width:88px;text-align:left">Lorem ipsum dolor sit amet, consectetur adipiscing elit, sed do eiusmod tempor incididunt ut labore et dolore magna aliqua. Lorem ipsum dolor sit amet, consectetur adipiscing elit, sed do eiusmod tempor incididunt ut labore et dolore magna aliqua.</div>
  <svg class="abs" style="left:233px;top:103px" width="10" height="70" viewBox="0 0 10 70"><path d="M1 0l7 4-7 4zM1 27l7 4-7 4zM1 54l7 4-7 4z" fill="var(--teal)"/></svg>
  <div class="abs" style="left:248px;top:101px;width:75px;font-size:3.4px;line-height:1.4;color:#444">
    <p style="height:27px">Lorem ipsum dolor sit amet, consectetur adipiscing elit, sed do eiusmod tempor</p>
    <p style="height:27px">Lorem ipsum dolor sit amet, consectetur adipiscing elit, sed do eiusmod tempor</p>
    <p>Lorem ipsum dolor sit amet, consectetur adipiscing elit, sed do eiusmod tempor</p>
  </div>
  <div class="foot"><span class="copy">Copyrighted content</span><span class="web">www.uLarkSlides.com</span><span class="num">12</span></div>
</section>

<!-- 12 intro statement -->
<section class="slide">
  <div class="brand"><i></i><span>uLark</span></div>
  <div class="title" style="top:12px">Title Goes Here</div>
  <div class="abs" style="left:150px;width:60px;top:31px;border-top:1px solid #888"></div>
  <div class="abs" style="left:16px;top:46px;width:3px;height:37px;background:var(--teal)"></div>
  <div class="abs" style="left:29px;top:44px;width:290px;font-size:5.6px;font-weight:700;line-height:1.45;text-align:justify">Lorem ipsum dolor sit amet, consectetur adipiscing elit, sed do eiusmod tempor incididunt ut labore et dolore magna aliqua. Ut enim ad minim veniam, quis nostrud exercitation ullamco laboris nisi ut aliquip extempor incididunt ut labore et dolore magna aliqua.</div>
  <div class="abs" style="left:20px;top:103px;width:300px;display:flex;justify-content:space-between;font-size:4.3px;line-height:1.45;color:#333">
    <div style="width:89px"><b style="display:block;margin-bottom:4px">Lorem ipsum dolor</b>Lorem ipsum dolor sit amet, on met consectetur elota adipiscing elit, sed do eiusmod tempor karamtam o kad mel etolik esti emka et.</div>
    <div style="width:89px"><b style="display:block;margin-bottom:4px">Lorem ipsum dolor</b>Lorem ipsum dolor sit amet, on met consectetur elota adipiscing elit, sed do eiusmod tempor karamtam o kad mel etolik esti emka et.</div>
    <div style="width:89px"><b style="display:block;margin-bottom:4px">Lorem ipsum dolor</b>Lorem ipsum dolor sit amet, on met consectetur elota adipiscing elit, sed do eiusmod tempor karamtam o kad mel etolik esti emka et.</div>
  </div>
  <div class="foot"><span class="copy">Copyrighted content</span><span class="web">www.uLarkSlides.com</span><span class="num">13</span></div>
</section>

<!-- 13 header band with icon circles -->
<section class="slide">
  <div class="abs" role="img" aria-label="Teal-tinted photo of modern architecture" style="left:0;right:0;top:0;height:96px;background:linear-gradient(120deg,#2b7383,#5f9ea8 55%,#3c8493)"></div>
  <div class="abs" style="left:0;right:0;top:32px;text-align:center;color:#fff;font-family:Roboto,Arial,sans-serif;font-weight:700;font-size:15px">Lorem ipsum dolor</div>
  <div class="abs" style="left:0;right:0;top:52px;text-align:center;color:#fff;font-size:4.6px">Lorem ipsum dolor sit amet, consectetur adipiscing elit</div>
  <svg class="abs" style="left:0;top:76px" width="335" height="40" viewBox="0 0 335 40">
    <g fill="#fff" stroke="#d6e6e8" stroke-width="1"><circle cx="76" cy="16" r="14"/><circle cx="167" cy="16" r="14"/><circle cx="259" cy="16" r="14"/></g>
    <circle cx="76" cy="16" r="10" fill="var(--teal)"/><circle cx="167" cy="16" r="10" fill="var(--teal)"/><circle cx="259" cy="16" r="10" fill="var(--teal)"/>
    <path d="M72 10h8v4a4 4 0 0 1-8 0zM76 18v3M73 22h6" stroke="#fff" stroke-width="1.3" fill="none"/>
    <circle cx="166" cy="15" r="3" fill="none" stroke="#fff" stroke-width="1.3"/><path d="M168 17l3 3" stroke="#fff" stroke-width="1.5"/>
    <circle cx="259" cy="14" r="3.5" fill="#fff"/><path d="M257 19h4" stroke="#fff" stroke-width="1.3"/>
  </svg>
  <div class="abs" style="left:40px;top:119px;width:270px;display:flex;justify-content:space-between;text-align:center">
    <div style="width:74px"><b style="font-size:4.6px;color:var(--teal);font-weight:600">Lorem ipsum dolor</b><p class="tx" style="margin-top:4px">Lorem ipsum dolor sit amet, no consectetur adipiscing elit, sed do eiusmod ti mo tempor incididunt ut labore et dolore magna aliqua. Ut labore et dolore magna aliqua.</p></div>
    <div style="width:74px"><b style="font-size:4.6px;color:var(--teal);font-weight:600">Lorem ipsum dolor</b><p class="tx" style="margin-top:4px">Lorem ipsum dolor sit amet, no consectetur adipiscing elit, sed do eiusmod ti mo tempor incididunt ut labore et dolore magna aliqua. Ut labore et dolore magna aliqua.</p></div>
    <div style="width:74px"><b style="font-size:4.6px;color:var(--teal);font-weight:600">Lorem ipsum dolor</b><p class="tx" style="margin-top:4px">Lorem ipsum dolor sit amet, no consectetur adipiscing elit, sed do eiusmod ti mo tempor incididunt ut labore et dolore magna aliqua. Ut labore et dolore magna aliqua.</p></div>
  </div>
  <div class="foot"><span class="copy">Copyrighted content</span><span class="web">www.uLarkSlides.com</span><span class="num">14</span></div>
</section>

<!-- 14 financial table -->
<section class="slide">
  <div class="brand"><i></i><span>uLark</span></div>
  <div class="title" style="top:11px;font-size:15px">Lorem ipsum dolor</div>
  <div class="abs" style="left:0;right:0;top:30px;text-align:center;font-size:4.6px;color:var(--teal)">Lorem ipsum dolor sit amet, consectetur adipiscing elit</div>
  <div class="abs" style="left:0;top:56px;width:17px;height:94px;background:var(--teal)"></div>
  <table class="fin abs" style="left:46px;top:50px;width:266px">
    <tr style="color:#fff"><td style="width:82px"></td><td style="width:10px"></td><th style="background:var(--teal);text-align:left">2019</th><th style="background:var(--teal);text-align:left">2020</th><th style="background:var(--teal);text-align:left">2021</th><th style="background:var(--teal);text-align:left">2022</th></tr>
    <tr style="background:#eef3f4"><td><b>Revenue</b></td><td></td><td></td><td></td><td></td><td></td></tr>
    <tr><td>Licence fees</td><td>£</td><td>1,787,100</td><td>6,177,000</td><td>10,807,000</td><td>12,580,000</td></tr>
    <tr style="background:#eef3f4"><td>Revenue share</td><td>£</td><td>630,000</td><td>11,474,750</td><td>15,414,000</td><td>15,414,000</td></tr>
    <tr><td>Development Fee Revenue</td><td>£</td><td>100,000</td><td>200,000</td><td>200,000</td><td>200,00</td></tr>
    <tr style="background:var(--teal-light);color:#fff"><td>Total Revenue</td><td>£</td><td>2,517,100</td><td>17,851,750</td><td>26,421,000</td><td>28,194,000</td></tr>
    <tr><td colspan="6" style="background:#eef3f4"></td></tr>
    <tr style="background:var(--teal-light);color:#fff"><td>Operating costs</td><td>£</td><td>1,408,910</td><td>2,522,838</td><td>2,852,835</td><td>2,979,113</td></tr>
    <tr><td colspan="6" style="background:#eef3f4"></td></tr>
    <tr style="background:var(--teal-light);color:#fff"><td>OPERATING PROFIT</td><td>£</td><td>1,108,190</td><td>15,328,912</td><td>23,568,165</td><td>25,214,887</td></tr>
    <tr><td colspan="6" style="background:#eef3f4"></td></tr>
    <tr style="background:var(--amber);color:#fff"><td>NET PROFIT</td><td>£</td><td>897,634</td><td>12,569,708</td><td>19,325,895</td><td>20,928,356</td></tr>
  </table>
  <div class="foot"><span class="copy">Copyrighted content</span><span class="web">www.uLarkSlides.com</span><span class="num">15</span></div>
</section>

<!-- 15 services -->
<section class="slide">
  <div class="brand"><i></i><span>uLark</span></div>
  <div class="title" style="top:14px">Our Services</div>
  <div class="abs" style="left:150px;width:60px;top:33px;border-top:1px solid #888"></div>
  <div class="abs" style="left:37px;top:52px;width:290px;display:grid;grid-template-columns:155px 130px;row-gap:10px">
    <div style="display:flex"><svg width="12" height="12" viewBox="0 0 12 12"><circle cx="6" cy="6" r="6" fill="var(--teal)"/><path d="M3 6l2 2 4-4" stroke="#fff" stroke-width="1.3" fill="none"/></svg><div style="width:88px;margin-left:5px;font-size:3.4px;line-height:1.4"><b>Lorem ipsum dolor</b><br>Lorem ipsum dolor sit amet, on met consectetur elota adipiscing elit, sed do eiusmod tempor karamtam o kad mel etolik esti emka et.</div></div>
    <div style="display:flex"><svg width="12" height="12" viewBox="0 0 12 12"><circle cx="6" cy="6" r="6" fill="var(--teal)"/><path d="M3 6l2 2 4-4" stroke="#fff" stroke-width="1.3" fill="none"/></svg><div style="width:88px;margin-left:5px;font-size:3.4px;line-height:1.4"><b>Lorem ipsum dolor</b><br>Lorem ipsum dolor sit amet, on met consectetur elota adipiscing elit, sed do eiusmod tempor karamtam o kad mel etolik esti emka et.</div></div>
    <div style="display:flex"><svg width="12" height="12" viewBox="0 0 12 12"><circle cx="6" cy="6" r="6" fill="var(--teal)"/><path d="M3 6l2 2 4-4" stroke="#fff" stroke-width="1.3" fill="none"/></svg><div style="width:88px;margin-left:5px;font-size:3.4px;line-height:1.4"><b>Lorem ipsum dolor</b><br>Lorem ipsum dolor sit amet, on met consectetur elota adipiscing elit, sed do eiusmod tempor karamtam o kad mel etolik esti emka et.</div></div>
    <div style="display:flex"><svg width="12" height="12" viewBox="0 0 12 12"><circle cx="6" cy="6" r="6" fill="var(--teal)"/><path d="M3 6l2 2 4-4" stroke="#fff" stroke-width="1.3" fill="none"/></svg><div style="width:88px;margin-left:5px;font-size:3.4px;line-height:1.4"><b>Lorem ipsum dolor</b><br>Lorem ipsum dolor sit amet, on met consectetur elota adipiscing elit, sed do eiusmod tempor karamtam o kad mel etolik esti emka et.</div></div>
    <div style="display:flex"><svg width="12" height="12" viewBox="0 0 12 12"><circle cx="6" cy="6" r="6" fill="var(--teal)"/><path d="M3 6l2 2 4-4" stroke="#fff" stroke-width="1.3" fill="none"/></svg><div style="width:88px;margin-left:5px;font-size:3.4px;line-height:1.4"><b>Lorem ipsum dolor</b><br>Lorem ipsum dolor sit amet, on met consectetur elota adipiscing elit, sed do eiusmod tempor karamtam o kad mel etolik esti emka et.</div></div>
    <div style="display:flex"><svg width="12" height="12" viewBox="0 0 12 12"><circle cx="6" cy="6" r="6" fill="var(--teal)"/><path d="M3 6l2 2 4-4" stroke="#fff" stroke-width="1.3" fill="none"/></svg><div style="width:88px;margin-left:5px;font-size:3.4px;line-height:1.4"><b>Lorem ipsum dolor</b><br>Lorem ipsum dolor sit amet, on met consectetur elota adipiscing elit, sed do eiusmod tempor karamtam o kad mel etolik esti emka et.</div></div>
  </div>
  <div class="foot"><span class="copy">Copyrighted content</span><span class="web">www.uLarkSlides.com</span><span class="num">16</span></div>
</section>

<!-- 16 positive / negative -->
<section class="slide">
  <div class="brand"><i></i><span>uLark</span></div>
  <div class="title" style="top:12px;font-size:15px">Lorem ipsum dolor</div>
  <div class="abs" style="left:150px;width:60px;top:33px;border-top:1px solid #888"></div>
  <svg class="abs" style="left:40px;top:39px" width="260" height="20" viewBox="0 0 260 20">
    <circle cx="11" cy="10" r="8" fill="none" stroke="var(--teal)" stroke-width="1.5"/><path d="M7 10l3 3 5-6" stroke="var(--teal)" stroke-width="1.5" fill="none"/>
    <circle cx="153" cy="10" r="8" fill="none" stroke="var(--amber)" stroke-width="1.5"/><path d="M150 7l6 6M156 7l-6 6" stroke="var(--amber)" stroke-width="1.5"/>
  </svg>
  <div class="abs" style="left:40px;top:62px;width:120px;height:110px;background:#f1f1f1">
    <div style="background:var(--teal);color:#fff;font-size:3.8px;font-weight:700;text-align:center;height:11px;line-height:11px">POSITIVE POINTS</div>
    <div style="padding:4px 6px;font-size:3.2px;line-height:1.4;color:#555">
      <p style="margin-bottom:5px;padding-left:13px;position:relative"><span style="position:absolute;left:0;top:1px;width:8px;height:8px;border-radius:50%;border:1px solid var(--teal)"></span><b style="color:#222">TITLE GOES HERE</b><br>Lorem ipsum dolor sit amet, consectetur adipiscing elit, sed do eiusmod tempor.</p>
      <p style="margin-bottom:5px;padding-left:13px;position:relative"><span style="position:absolute;left:0;top:1px;width:8px;height:8px;border-radius:50%;border:1px solid var(--teal)"></span><b style="color:#222">TITLE GOES HERE</b><br>Lorem ipsum dolor sit amet, consectetur adipiscing elit, sed do eiusmod tempor.</p>
      <p style="margin-bottom:5px;padding-left:13px;position:relative"><span style="position:absolute;left:0;top:1px;width:8px;height:8px;border-radius:50%;border:1px solid var(--teal)"></span><b style="color:#222">TITLE GOES HERE</b><br>Lorem ipsum dolor sit amet, consectetur adipiscing elit, sed do eiusmod tempor.</p>
      <p style="padding-left:13px;position:relative"><span style="position:absolute;left:0;top:1px;width:8px;height:8px;border-radius:50%;border:1px solid var(--teal)"></span><b style="color:#222">TITLE GOES HERE</b><br>Lorem ipsum dolor sit amet, consectetur adipiscing elit, sed do eiusmod tempor.</p>
    </div>
  </div>
  <div class="abs" style="left:184px;top:62px;width:120px;height:110px;background:#f1f1f1">
    <div style="background:var(--amber);color:#fff;font-size:3.8px;font-weight:700;text-align:center;height:11px;line-height:11px">NEGATIVE POINTS</div>
    <div style="padding:4px 6px;font-size:3.2px;line-height:1.4;color:#555">
      <p style="margin-bottom:5px;padding-left:13px;position:relative"><span style="position:absolute;left:0;top:1px;width:8px;height:8px;border-radius:50%;border:1px solid var(--amber)"></span><b style="color:var(--amber)">TITLE GOES HERE</b><br>Lorem ipsum dolor sit amet, consectetur adipiscing elit, sed do eiusmod tempor.</p>
      <p style="margin-bottom:5px;padding-left:13px;position:relative"><span style="position:absolute;left:0;top:1px;width:8px;height:8px;border-radius:50%;border:1px solid var(--amber)"></span><b style="color:var(--amber)">TITLE GOES HERE</b><br>Lorem ipsum dolor sit amet, consectetur adipiscing elit, sed do eiusmod tempor.</p>
      <p style="margin-bottom:5px;padding-left:13px;position:relative"><span style="position:absolute;left:0;top:1px;width:8px;height:8px;border-radius:50%;border:1px solid var(--amber)"></span><b style="color:var(--amber)">TITLE GOES HERE</b><br>Lorem ipsum dolor sit amet, consectetur adipiscing elit, sed do eiusmod tempor.</p>
      <p style="padding-left:13px;position:relative"><span style="position:absolute;left:0;top:1px;width:8px;height:8px;border-radius:50%;border:1px solid var(--amber)"></span><b style="color:var(--amber)">TITLE GOES HERE</b><br>Lorem ipsum dolor sit amet, consectetur adipiscing elit, sed do eiusmod tempor.</p>
    </div>
  </div>
  <div class="foot"><span class="copy">Copyrighted content</span><span class="web">www.uLarkSlides.com</span><span class="num">17</span></div>
</section>

<!-- 17 org chart -->
<section class="slide">
  <div class="brand"><i></i><span>uLark</span></div>
  <div class="title" style="top:12px;font-size:15px">Lorem ipsum dolor</div>
  <div class="abs" style="left:150px;width:60px;top:33px;border-top:1px solid #888"></div>
  <svg class="abs" style="left:0;top:40px" width="335" height="140" viewBox="0 0 335 140" font-family="Roboto,Arial,sans-serif" text-anchor="middle">
    <g stroke="#999" stroke-width=".6" fill="none">
      <path d="M167 18v8M66 26h201M66 26v4M167 26v4M267 26v4"/>
      <path d="M38 50v94M38 66h16M38 94h16M38 122h16"/>
      <path d="M138 50v94M138 66h16M138 94h16M138 122h16"/>
      <path d="M238 50v94M238 66h16M238 94h16M238 122h16"/>
    </g>
    <rect x="132" y="2" width="70" height="8" fill="var(--teal)"/><rect x="132" y="10" width="70" height="7" fill="var(--mint)"/>
    <text x="167" y="7.5" font-size="3.8" fill="#fff">FIRST / LAST NAME</text><text x="167" y="15" font-size="3" fill="#fff">Position</text>
    <g font-size="3.8">
      <rect x="32" y="30" width="70" height="8" fill="var(--mint)"/><rect x="32" y="38" width="70" height="8" fill="var(--amber)"/><text x="67" y="35.5" fill="#fff">FIRST / LAST NAME</text><text x="67" y="43.5" font-size="3" fill="#fff">Position</text>
      <rect x="132" y="30" width="70" height="8" fill="var(--mint)"/><rect x="132" y="38" width="70" height="8" fill="var(--amber)"/><text x="167" y="35.5" fill="#fff">FIRST / LAST NAME</text><text x="167" y="43.5" font-size="3" fill="#fff">Position</text>
      <rect x="232" y="30" width="70" height="8" fill="var(--mint)"/><rect x="232" y="38" width="70" height="8" fill="var(--amber)"/><text x="267" y="35.5" fill="#fff">FIRST / LAST NAME</text><text x="267" y="43.5" font-size="3" fill="#fff">Position</text>
    </g>
    <g font-size="3.4" fill="#888">
      <g fill="#f0f0f0" stroke="#ccc" stroke-width=".5">
        <rect x="54" y="60" width="46" height="7"/><rect x="54" y="68" width="46" height="7" fill="#ddd"/>
        <rect x="54" y="88" width="46" height="7"/><rect x="54" y="96" width="46" height="7" fill="#ddd"/>
        <rect x="54" y="116" width="46" height="7"/><rect x="54" y="124" width="46" height="7" fill="#ddd"/>
        <rect x="154" y="60" width="46" height="7"/><rect x="154" y="68" width="46" height="7" fill="#ddd"/>
        <rect x="154" y="88" width="46" height="7"/><rect x="154" y="96" width="46" height="7" fill="#ddd"/>
        <rect x="154" y="116" width="46" height="7"/><rect x="154" y="124" width="46" height="7" fill="#ddd"/>
        <rect x="254" y="60" width="46" height="7"/><rect x="254" y="68" width="46" height="7" fill="#ddd"/>
        <rect x="254" y="88" width="46" height="7"/><rect x="254" y="96" width="46" height="7" fill="#ddd"/>
        <rect x="254" y="116" width="46" height="7"/><rect x="254" y="124" width="46" height="7" fill="#ddd"/>
      </g>
      <text x="77" y="65">FIRST / LAST NAME</text><text x="77" y="73" font-size="2.8">Position</text>
      <text x="77" y="93">FIRST / LAST NAME</text><text x="77" y="101" font-size="2.8">Position</text>
      <text x="77" y="121">FIRST / LAST NAME</text><text x="77" y="129" font-size="2.8">Position</text>
      <text x="177" y="65">FIRST / LAST NAME</text><text x="177" y="73" font-size="2.8">Position</text>
      <text x="177" y="93">FIRST / LAST NAME</text><text x="177" y="101" font-size="2.8">Position</text>
      <text x="177" y="121">FIRST / LAST NAME</text><text x="177" y="129" font-size="2.8">Position</text>
      <text x="277" y="65">FIRST / LAST NAME</text><text x="277" y="73" font-size="2.8">Position</text>
      <text x="277" y="93">FIRST / LAST NAME</text><text x="277" y="101" font-size="2.8">Position</text>
      <text x="277" y="121">FIRST / LAST NAME</text><text x="277" y="129" font-size="2.8">Position</text>
    </g>
  </svg>
  <div class="foot"><span class="copy">Copyrighted content</span><span class="web">www.uLarkSlides.com</span><span class="num">18</span></div>
</section>

<!-- 18 world infographic -->
<section class="slide">
  <div class="brand"><i></i><span>uLark</span></div>
  <div class="abs" role="img" aria-label="Faint world map in the background" style="left:40px;right:40px;top:20px;height:110px;background:radial-gradient(ellipse at center,#eef3f4,#fff 70%)"></div>
  <div class="title" style="top:12px;font-size:15px">Lorem ipsum dolor</div>
  <div class="abs" style="left:150px;width:60px;top:33px;border-top:1px solid #888"></div>
  <div class="abs" style="left:50px;top:48px;width:235px;text-align:center;font-size:4.2px;line-height:1.5;color:#333">Sed ut perspiciatis, unde omnis iste natus error sit voluptatem accusantium doloremque laudantium, totam rem aperiam eaque ipsa, quae ab illo inventore veritatis et quasi architecto beatae vitae dicta sunt, explicabo. <b>Nemo enim ipsam voluptatem,</b> quia voluptas sit, aspernatur aut odit aut fugit, sed quia consequuntur magni dolores eos, qui ratione <b>voluptatem sequi nesciunt,</b> neque porro quisquam est.</div>
  <div class="abs" style="left:0;right:0;top:109px;height:80px;background:var(--teal-mid)"></div>
  <div class="abs" style="left:24px;top:119px;color:#fff;font-family:Roboto,Arial,sans-serif;font-weight:700;font-size:10.5px;line-height:1.35">Worldmap<br>Infographic</div>
  <div class="abs" style="left:24px;top:150px;width:95px;color:#fff;font-size:3.4px;line-height:1.45">Lorem ipsum dolor sit amet, on met consectetur elota adipiscing elit, sed do eiusmod tempor karamtam o kad mel etolik esti emka et.</div>
  <svg class="abs" style="left:180px;top:118px" width="100" height="56" viewBox="0 0 100 56" font-family="Roboto,Arial,sans-serif" font-size="6" text-anchor="middle">
    <circle cx="23" cy="28" r="18" fill="none" stroke="#fff" stroke-width="4"/>
    <circle cx="23" cy="28" r="18" fill="none" stroke="var(--amber)" stroke-width="4" stroke-dasharray="67.9 113.1" transform="rotate(-90 23 28)"/>
    <circle cx="23" cy="28" r="11" fill="var(--amber)"/><text x="23" y="30" fill="#fff">60%</text>
    <circle cx="78" cy="28" r="18" fill="none" stroke="#fff" stroke-width="4"/>
    <circle cx="78" cy="28" r="18" fill="none" stroke="var(--teal-dark)" stroke-width="4" stroke-dasharray="45.2 113.1" transform="rotate(-90 78 28)"/>
    <circle cx="78" cy="28" r="11" fill="var(--teal)"/><text x="78" y="30" fill="#fff">40%</text>
  </svg>
  <div class="foot" style="border-top-color:transparent"><span class="copy" style="color:#dfeeee">Copyrighted content</span><span class="web" style="color:#fff">www.uLarkSlides.com</span><span class="num" style="background:var(--teal-dark)">19</span></div>
</section>

</div>
</body>
</html>
```